Business Card Tevan Law llc examples and ideas are attached.

in addition to the logo we need a desription what we do: "Reprsenting students with disabilites obtain services to progress in the public school system."

If you can squeeze it on the fron at the bottom great if not put it on the back

```html
<!DOCTYPE html>
<html lang="en">
<head>
<meta charset="utf-8">
<title>Tevan Law llc – Business Card</title>
<link rel="stylesheet" href="https://fonts.googleapis.com/css2?family=Arimo&family=Bitter:ital,wght@0,700;1,700&family=EB+Garamond&family=Open+Sans&display=swap">
<style>
  :root {
    --page: #ffffff;
    --card: #a3d5f2;
    --ink: #111111;
    --navy: #0c3060;
  }
  html, body {
    margin: 0;
    padding: 0;
    width: 1200px;
    height: 719px;
    overflow: hidden;
    background: var(--page);
  }
  .card {
    position: absolute;
    left: 42px;
    top: 40px;
    width: 1115px;
    height: 637px;
    background: var(--card);
    color: var(--ink);
  }
  .brand-mark {
    position: absolute;
    left: 40px;
    top: 150px;
    display: flex;
    align-items: center;
    gap: 18px;
  }
  .brand-mark__square {
    width: 46px;
    height: 46px;
    background: var(--navy);
  }
  .brand-mark__name {
    font-family: "Bitter", serif;
    font-weight: 700;
    font-size: 48px;
    color: var(--navy);
    white-space: nowrap;
  }
  .divider {
    position: absolute;
    left: 455px;
    top: 156px;
    width: 5px;
    height: 351px;
    background: var(--ink);
  }
  .details {
    position: absolute;
    left: 531px;
    top: 0;
    white-space: nowrap;
  }
  .details p { margin: 0; position: absolute; left: 0; }
  .firm-name {
    top: 12px;
    font-family: "Bitter", serif;
    font-weight: 700;
    font-size: 50px;
  }
  .attorney-name {
    top: 126px;
    font-family: "Arimo", sans-serif;
    font-size: 42px;
  }
  .attorney-title {
    top: 169px;
    font-family: "EB Garamond", serif;
    font-size: 33px;
  }
  .street {
    top: 230px;
    font-family: "Bitter", serif;
    font-weight: 700;
    font-size: 39px;
  }
  .street sup { font-size: 20px; font-style: italic; vertical-align: 16px; line-height: 0; }
  .city {
    top: 272px;
    font-family: "EB Garamond", serif;
    font-size: 38px;
  }
  .hours {
    top: 316px;
    font-family: "Open Sans", sans-serif;
    font-size: 29px;
  }
  .phone, .email {
    font-family: "Bitter", serif;
    font-weight: 700;
    font-style: italic;
    font-size: 36px;
  }
  .phone { top: 382px; }
  .email { top: 435px; }
  .tagline {
    position: absolute;
    left: 0;
    right: 0;
    top: 556px;
    margin: 0;
    text-align: center;
    font-family: "Bitter", serif;
    font-weight: 700;
    font-style: italic;
    font-size: 19px;
  }
</style>
</head>
<body>
  <div class="card">
    <div class="brand-mark">
      <span class="brand-mark__square"></span>
      <span class="brand-mark__name">Tevan Law</span>
    </div>
    <div class="divider"></div>
    <div class="details">
      <p class="firm-name">Tevan Law llc</p>
      <p class="attorney-name">Dorian K Tevan</p>
      <p class="attorney-title">Attorney at low</p>
      <p class="street">4115 NE 18<sup>th</sup> Ave</p>
      <p class="city">Harbor Point FL 33410</p>
      <p class="hours">By appointment only</p>
      <p class="phone">+813 555 0147</p>
      <p class="email">dory?tevanlaw@mailbox.com</p>
    </div>
    <p class="tagline">Reprsenting students with disabilites obtain services to progress in the public school system</p>
  </div>
</body>
</html>
```